Hal's Remedies Business Card Design Project

I need a business card designed for my pharmacy Hal's Remedies. I would like just the logo on one side, maybe with black background and white lettering. The other side I would also like to include my logo which is attached. Also, please include my name and the following information:
Hal Norwick Owner/Pharm D.
Business address is 7163 N Birch Rd Sioux Falls, SD 57291.
Phone number is 605-318-6027 and fax # is 605-318-6031.
my email address is hal@halsremedies.example.
My website is www.halsremedies.example.
My business hours are Monday-Friday 8am-7 pm. Saturday 8am-12 pm. Sunday Closed.
I would like the design to include my logo colors, black, white, and neon green. Silver may be added as a highlight. Thanks.
Pharmacy
See above in product description

```html
<!DOCTYPE html>
<html lang="en">
<head>
<meta charset="utf-8">
<title>Hal's Remedies – Business Card</title>
<link rel="stylesheet" href="https://fonts.googleapis.com/css2?family=Open+Sans:ital,wght@0,400;0,600;0,700;1,400&display=swap">
<style>
  :root {
    --stage: #3b3b3b;
    --card-white: #ffffff;
    --card-black: #0e0e0e;
    --ink: #2b2b2b;
    --ink-soft: #4a4a4a;
    --neon: #a4cd39;
    --line: #3a3a3a;
  }
  * { margin: 0; padding: 0; box-sizing: border-box; }
  html, body { width: 1200px; height: 871px; overflow: hidden; }
  body {
    background: var(--stage);
    font-family: "Open Sans", Arial, sans-serif;
    position: relative;
  }

  .card { position: absolute; border-radius: 4px; overflow: hidden; }

  /* Back side: black with logo name */
  .card-back {
    left: 80px; top: 60px; width: 500px; height: 286px;
    background: var(--card-black);
    display: flex; align-items: center; justify-content: center; gap: 16px;
  }
  .card-back .brand-dot { width: 22px; height: 22px; border-radius: 50%; background: var(--neon); }
  .card-back .brand-name { color: #fff; font-weight: 700; font-size: 40px; letter-spacing: -0.5px; }

  /* Front side */
  .card-front {
    left: 420px; top: 400px; width: 700px; height: 400px;
    background: var(--card-white);
    color: var(--ink);
  }

  .title-band {
    position: absolute; right: 0; top: 48px; width: 330px; height: 70px;
    background: var(--neon);
    border-radius: 35px 0 0 35px;
    padding: 12px 0 0 36px;
    color: #fff;
  }
  .title-band .person { font-weight: 600; font-size: 16px; letter-spacing: 0.3px; }
  .title-band .role { font-style: italic; font-size: 14px; margin-top: 2px; }

  .brand {
    position: absolute; left: 48px; top: 138px;
    display: flex; align-items: center; gap: 16px;
  }
  .brand .brand-dot { width: 26px; height: 26px; border-radius: 50%; background: var(--neon); }
  .brand .divider { width: 1.5px; height: 66px; background: var(--line); }
  .brand .brand-name { font-weight: 700; font-size: 36px; letter-spacing: -0.8px; color: var(--ink); }

  .contact { position: absolute; font-size: 15px; color: var(--ink-soft); line-height: 1.35; }
  .contact .row { display: flex; gap: 12px; align-items: flex-start; margin-bottom: 6px; }
  .contact svg { flex: none; margin-top: 2px; }

  .contact-left { left: 48px; top: 232px; width: 260px; }
  .contact-right { left: 360px; top: 242px; width: 320px; font-size: 16px; }
  .contact-right .phone { letter-spacing: 1.5px; }
</style>
</head>
<body>

  <section class="card card-back" aria-label="Card back">
    <span class="brand-dot"></span>
    <span class="brand-name">Hal's Remedies</span>
  </section>

  <section class="card card-front" aria-label="Card front">
    <div class="title-band">
      <div class="person">Hal Norwick Owner/Pharm D.</div>
      <div class="role">Head of Sales Manager</div>
    </div>

    <div class="brand">
      <span class="brand-dot"></span>
      <span class="divider"></span>
      <span class="brand-name">Hal's Remedies</span>
    </div>

    <div class="contact contact-left">
      <div class="row">
        <svg width="14" height="18" viewBox="0 0 14 18" aria-hidden="true"><path d="M7 0a7 7 0 0 0-7 7c0 5 7 11 7 11s7-6 7-11a7 7 0 0 0-7-7z" fill="var(--neon)"/><circle cx="7" cy="7" r="2.5" fill="#fff"/></svg>
        <span>7163 N Birch Rd Sioux Falls,<br>SD 57291.</span>
      </div>
      <div class="row">
        <svg width="16" height="12" viewBox="0 0 16 12" aria-hidden="true"><rect x="0.75" y="0.75" width="14.5" height="10.5" fill="none" stroke="var(--neon)" stroke-width="1.5"/><path d="M1 1l7 6 7-6" fill="none" stroke="var(--neon)" stroke-width="1.5"/></svg>
        <span>hal@halsremedies.example</span>
      </div>
    </div>

    <div class="contact contact-right">
      <div class="row">
        <svg width="16" height="16" viewBox="0 0 16 16" aria-hidden="true"><path d="M3 1l3 3-1.5 2a9 9 0 0 0 5.5 5.5L12 10l3 3-2 2C7 15 1 9 1 3z" fill="var(--neon)"/></svg>
        <span class="phone">605 - 318 - 6027</span>
      </div>
      <div class="row">
        <svg width="18" height="16" viewBox="0 0 18 16" aria-hidden="true"><rect x="4" y="1" width="10" height="5" fill="var(--neon)"/><rect x="1" y="6" width="16" height="8" rx="1" fill="var(--neon)"/><rect x="5" y="10" width="8" height="5" fill="#fff" stroke="var(--neon)"/></svg>
        <span class="phone">605 - 318 - 6031</span>
      </div>
      <div class="row">
        <svg width="16" height="16" viewBox="0 0 16 16" aria-hidden="true"><circle cx="8" cy="8" r="7" fill="none" stroke="var(--neon)" stroke-width="1.5"/><path d="M8 4v4h3" fill="none" stroke="var(--neon)" stroke-width="1.5"/></svg>
        <span>Monday-Friday 8am-7 pm<br>Saturday 8am-12 pm. Sunday Closed.</span>
      </div>
    </div>
  </section>

</body>
</html>
```